Sophisticated, clean website reflecting my feminine, playful side to sell my abstract art,

I need a website no more than 3 pages to showcase my paintings, a little about me and some contact info. I do abstracts so looking for something a little edgy, yet feminine and current.
Updates

Hi there, These are some artists websites that I Iike: Mirabelvoss.com (I like how airy it is) tobiasmerrowind.com kevinplodderas.com (I like how it scrolls) I'll need a place for a photo ( a headshot-i do not have it yet so I'll need to be able to upload that later) as well as an area for my bio. Also, it's important that I will be able to upload any new photos and descriptions easily so it should be user friendly. Lastly, I like in a sunny place so would like to have this seem upbeat and playful as that is how i like to paint. thanks-I'm trying to upload my photos now -

Target Market(s)

ppl ages 35-70 who want large scale art for their homes

Industry/Entity Type

art

Coding

Coded - Design and coding required

Number of Pages Required

3 page

Colors

Designer to choose colors to be used in the design.

Requirements
Must have
• photos of my art, a place for my bio, be easy to reach me. tasteful-nothing too "in your face" -my clients are pretty high end and organized. They like clean lines
Nice to have
• sophisticated background, muted tones in the back-similar clean font throughout-no cursive
Should not have
• too many dark areas. Too many blocks of color. Too serious.

```html
<!DOCTYPE html>
<html lang="en">
<head>
<meta charset="utf-8">
<title>Marisol Keane Art</title>
<link rel="stylesheet" href="https://fonts.googleapis.com/css2?family=Cinzel+Decorative:wght@400;700&family=Lora:wght@400;700&family=Open+Sans:wght@400;700&family=Cormorant+Garamond:ital,wght@0,500;1,500&display=swap">
<style>
:root{
  --pink:#e6007e;
  --blush:#ffb8ff;
  --plum:#7a1380;
  --ink:#1d1d1d;
  --paper:#ffffff;
  --mist:#e9e8e8;
  --night:#0d0d16;
  --rule:#8a8a8a;
}
*{box-sizing:border-box;margin:0;padding:0}
html,body{width:1200px;height:2906px;overflow:hidden;background:var(--paper)}
body{position:relative;font-family:"Lora",serif;color:var(--ink)}
.promo-bar{position:absolute;top:0;left:0;width:1200px;height:38px;background:var(--blush);display:flex;align-items:center;justify-content:center;font-family:"Cormorant Garamond",serif;font-style:italic;font-size:16px}
.site-header{position:absolute;top:38px;left:0;width:1200px;height:69px;display:flex;align-items:center;padding:0 97px}
.brand{font-family:"Cinzel Decorative",serif;font-weight:700;font-size:25px;color:var(--plum)}
.main-nav{margin-left:auto;display:flex;align-items:center;gap:52px;font-family:"Cinzel Decorative",serif;font-size:15px}
.cart-btn{width:30px;height:30px;margin-left:-20px}
.hero{position:absolute;top:107px;left:0;width:1200px;height:561px;background:linear-gradient(120deg,#2e2a33 0%,#3b3838 35%,#2a3a30 55%,#3f3a2c 80%,#2c2b35 100%);text-align:center;color:#fff}
.hero::before,.hero::after{content:"";position:absolute;top:0;width:14px;height:100%;background:#121212}
.hero::before{left:390px}.hero::after{left:794px}
.hero-kicker{position:relative;padding-top:175px;font-family:"Cinzel Decorative",serif;font-size:58px;line-height:1}
.hero-title{position:relative;margin-top:18px;font-family:"Cinzel Decorative",serif;font-weight:700;font-size:74px;line-height:1}
.btn{display:inline-block;background:var(--pink);color:#fff;border-radius:30px}
.hero .btn{position:relative;margin-top:45px;width:166px;height:57px;line-height:57px;font-family:"Cinzel Decorative",serif;font-size:24px}
.about-photo{position:absolute;top:759px;left:0;width:608px;height:485px;background:linear-gradient(135deg,#c9c6bd,#8f9a8a 45%,#6b7356 70%,#b7b0a3);box-shadow:0 4px 12px rgba(0,0,0,.3)}
.about-panel{position:absolute;top:795px;left:608px;width:592px;height:414px;background:var(--mist);padding:16px 50px 0 51px}
.about-panel h2{font-family:"Cinzel Decorative",serif;font-size:34px;font-weight:700}
.about-panel p{margin-top:20px;font-size:15px;line-height:25.7px}
.about-panel .btn{margin-top:25px;padding:0 15px;height:43px;line-height:43px;font-size:15px;font-weight:700}
.gallery-title{position:absolute;top:1320px;width:1200px;text-align:center;font-family:"Cinzel Decorative",serif;font-weight:700;font-size:42px}
.work{position:absolute;width:319px;text-align:center}
.work .canvas{height:319px;border-radius:4px;box-shadow:0 2px 6px rgba(0,0,0,.2)}
.work h3{margin-top:30px;font-family:"Cinzel Decorative",serif;font-weight:700;font-size:23px}
.contact{position:absolute;top:2279px;left:0;width:1200px;height:627px;background:linear-gradient(135deg,#0c0c14,#1a1624 50%,#0b0b10);color:#fff}
.contact-info{position:absolute;left:98px;top:90px;width:345px;font-family:"Open Sans",sans-serif}
.contact-info h2{font-family:"Cinzel Decorative",serif;font-size:40px;font-weight:400;white-space:nowrap}
.info-row{display:flex;align-items:flex-start;gap:12px;font-size:16px;line-height:26px}
.info-row svg{flex:none;width:38px;height:38px}
.social h4{margin-top:46px;font-size:15px;font-weight:700}
.social-links{display:flex;gap:12px;margin-top:16px}
.social-links span{width:30px;height:30px;border-radius:50%;background:#fff}
.enquiry{position:absolute;left:465px;top:77px;width:640px;height:436px;background:var(--mist);border-radius:18px;padding:24px 40px;color:var(--ink)}
.enquiry h2{font-family:"Cinzel Decorative",serif;font-weight:400;font-size:28px;color:#444;margin-left:6px}
.fields{display:grid;grid-template-columns:270px 270px;gap:14px 22px;margin-top:22px}
.field{height:53px;border-radius:27px;background:#fff;font-size:12px;color:#555;padding:18px 25px}
.field.message{grid-column:1/3;height:118px;margin-top:7px}
.enquiry .submit{margin:25px 0 0 16px;width:91px;height:42px;line-height:42px;text-align:center;background:var(--pink);color:#fff;border-radius:4px;font-family:"Open Sans",sans-serif;font-size:17px}
.footer-rule{position:absolute;left:98px;top:538px;width:1000px;border-top:1px dashed var(--rule)}
.copyright{position:absolute;top:575px;width:1200px;text-align:center;font-family:"Cormorant Garamond",serif;font-size:16px;font-variant:small-caps;letter-spacing:.5px}
</style>
</head>
<body>
<div class="promo-bar">Lorem ipsum dolor sit amet, consectetur adipiscing elit, sed do eiusmod</div>

<header class="site-header">
  <div class="brand">Marisol Keane Art</div>
  <nav class="main-nav">
    <span>Home</span><span>About Me</span><span>Abstracts</span><span>Contact Us</span>
    <svg class="cart-btn" viewBox="0 0 30 30" aria-label="Cart"><circle cx="15" cy="15" r="13.5" fill="none" stroke="#e6007e" stroke-width="1.5"/><path d="M8 10h2l2 7h8l2-5H11" fill="none" stroke="#e6007e" stroke-width="1.6"/><circle cx="13" cy="20" r="1.2" fill="#e6007e"/><circle cx="19" cy="20" r="1.2" fill="#e6007e"/></svg>
  </nav>
</header>

<section class="hero" role="img" aria-label="Dimmed triptych of abstract paintings behind the welcome text">
  <div class="hero-kicker">Welcome to</div>
  <div class="hero-title">Marisol Keane Art</div>
  <span class="btn">Arts</span>
</section>

<div class="about-photo" role="img" aria-label="Photo of the artist beside her easel in the studio"></div>
<section class="about-panel">
  <h2>About Me</h2>
  <p>Sed ut perspiciatis unde omnis iste natus error sit voluptatem accusantium doloremque laudantium, totam rem aperiam, eaque ipsa quae ab illo inventore veritatis et quasi architecto beatae vitae dicta sunt explicabo. Nemo enim ipsam voluptatem quia voluptas sit aspernatur aut odit aut fugit, sed quia consequuntur magni dolores eos qui ratione voluptatem sequi nesciunt. Neque porro quisquam est, qui dolorem ipsum quia dolor sit amet, consectetur, adipisci velit, sed quia non numquam eius modi tempora incidunt ut labore et dolore magnam aliquam quaerat voluptatem.</p>
  <span class="btn">Learn More</span>
</section>

<h2 class="gallery-title">Abstracts Painting</h2>
<div class="work" style="left:90px;top:1410px"><div class="canvas" role="img" aria-label="Abstract painting in yellow and blue" style="background:linear-gradient(135deg,#efe9dc,#d9c37a 40%,#5a7fb0 70%,#efeae2)"></div><h3>Citrus Morning</h3></div>
<div class="work" style="left:434px;top:1410px"><div class="canvas" role="img" aria-label="Abstract painting with blue drips" style="background:linear-gradient(180deg,#cfc9bd 0%,#4f8fbf 15%,#a9c6d6 45%,#d6d6d0 100%)"></div><h3>Rainfall</h3></div>
<div class="work" style="left:778px;top:1410px"><div class="canvas" role="img" aria-label="Abstract painting in pinks and maroon" style="background:radial-gradient(circle at 55% 55%,#c99aa6,#e8c6cc 45%,#8a4a52 80%,#efdadd)"></div><h3>Petal Dance</h3></div>
<div class="work" style="left:90px;top:1813px"><div class="canvas" role="img" aria-label="Abstract painting with red loops" style="background:linear-gradient(135deg,#8b3a2c,#c87a60 30%,#eee6e0 60%,#efe9e4)"></div><h3>Crimson Loop</h3></div>
<div class="work" style="left:434px;top:1813px"><div class="canvas" role="img" aria-label="Abstract painting with teal burst" style="background:radial-gradient(circle at 55% 60%,#1d1d1d,#2f8a8a 40%,#c68a3a 70%,#e6e1d6)"></div><h3>Tidal Burst Study</h3></div>
<div class="work" style="left:778px;top:1813px"><div class="canvas" role="img" aria-label="Abstract painting in deep brown" style="background:linear-gradient(135deg,#e9e3dc,#6e2a22 45%,#a7584a 65%,#ece6e0)"></div><h3>Ember</h3></div>

<footer class="contact">
  <div class="contact-info">
    <h2>Contact Info</h2>
    <div class="info-row" style="margin-top:34px"><svg viewBox="0 0 38 38"><circle cx="19" cy="19" r="19" fill="#e6007e"/><path d="M19 11a6 6 0 0 0-6 6c0 4.5 6 10 6 10s6-5.5 6-10a6 6 0 0 0-6-6z" fill="#fff"/><circle cx="19" cy="17" r="2" fill="#e6007e"/></svg><span style="margin-top:5px">Lorem ipsum dolor sit amet, consectetur<br>adipiscing</span></div>
    <div class="info-row" style="margin-top:50px"><svg viewBox="0 0 38 38"><circle cx="19" cy="19" r="19" fill="#e6007e"/><rect x="11" y="13" width="16" height="12" rx="1.5" fill="#fff"/><path d="M11 14l8 6 8-6" fill="none" stroke="#e6007e" stroke-width="1.5"/></svg><span style="margin-top:6px">info@marisolkeaneart.com</span></div>
    <div class="info-row" style="margin-top:28px"><svg viewBox="0 0 38 38"><circle cx="19" cy="19" r="19" fill="#e6007e"/><path d="M14 12c-1.5 1-2 3 0 6.5s5 6 7.5 6.5c2 .5 3.5-1 4-2l-3-2.5-1.5 1.3c-1.5-.6-3.5-2.6-4-4l1.3-1.5z" fill="#fff"/></svg><span style="margin-top:6px">+1555-010-2468</span></div>
    <div class="social"><h4>SOCIAL MEDIA</h4><div class="social-links" aria-label="Social media links"><span></span><span></span><span></span><span></span></div></div>
  </div>
  <form class="enquiry">
    <h2>Get in Touch</h2>
    <div class="fields">
      <div class="field">First Name*</div><div class="field">Last Name*</div>
      <div class="field">Email*</div><div class="field">Phone*</div>
      <div class="field message">Tell me about your case*</div>
    </div>
    <div class="submit">SUBMIT</div>
  </form>
  <div class="footer-rule"></div>
  <div class="copyright">© Copyrights 2022 © Marisol Keane Art | All Rights Reserved</div>
</footer>
</body>
</html>
```